Nova crest cleansers Trading L.L.C

We need stationary design for our new company contain ( Business card - head latter - envelops( big & small) - folder file ) One identity and creative design & has related with logo colors ....A unified identity
The main elements of the design that includes the main logos (logo crest + crest logo membership Khalid bin Nasser) as it is in the attachment then the address of the company.
The Address is
Ras Hamdan - Next to Corniche Plaza Mall
Noor Trade Tower Building - 604
P.O.Box : 47819 Dubai - U.A.E
Tel. : 00971 4 58 71 204
Fax : 00971 4 58 71 205
Email : info@novacrestcleansers.example
www.novacrestcleansers.example
Please read the attachment in an important way, especially the terms of the government logo (Khalid Bin Nasser Membership)
In the design of business cards .. Please put slogans (Oru fresh home - Oru Professional - Faraheed ) be in the back of the card
Put my name sample
Samir Youssef Abdul Karim
Director Manager
Mobil : + 971 52 387 0 387

```html
<!DOCTYPE html>
<html lang="en">
<head>
<meta charset="utf-8">
<title>Nova crest cleansers Trading L.L.C — Stationery</title>
<link href="https://fonts.googleapis.com/css2?family=Didact+Gothic&family=Roboto:wght@400;500&family=Roboto+Condensed:wght@700&display=swap" rel="stylesheet">
<style>
:root{
  --bg:#dddddd;
  --paper:#ffffff;
  --blue:#0a6fc2;
  --green:#6cbf3a;
  --ink:#4a4a4a;
  --rule:#8a8a8a;
  --red:#e0322c;
  --partner:#3f9a35;
}
*{margin:0;padding:0;box-sizing:border-box}
html,body{width:1200px;height:738px;overflow:hidden;background:var(--bg)}
.canvas{position:relative;width:1200px;height:738px;font-family:"Roboto",sans-serif}
.sheet{position:absolute;background:var(--paper);box-shadow:0 1px 3px rgba(0,0,0,.12);overflow:hidden}

.tab{position:absolute;left:0;width:13px;background:var(--green);border-radius:0 12px 12px 0}
.band{position:absolute;right:0;background:var(--blue);border-radius:12px 0 0 12px;color:#fff;font-size:6.2px;line-height:1.3}
.brand{position:absolute;display:flex;align-items:center;gap:5px}
.brand-dot{border-radius:50%;background:var(--green);flex:none}
.brand-name{font-family:"Roboto",sans-serif;font-weight:400;color:var(--blue);white-space:nowrap;letter-spacing:-.3px}

.contact{list-style:none}
.contact li{display:flex;align-items:center;gap:4px;height:8px}
.contact svg{width:6px;height:6px;fill:#fff;flex:none}

/* letterhead */
.letterhead{left:66px;top:74px;width:452px;height:583px}
.letterhead .tab{top:43px;height:50px}
.letterhead .band{top:43px;width:277px;height:50px}
.letterhead .brand{left:41px;top:54px}
.letterhead .address{position:absolute;left:14px;top:18px;font-weight:500}
.letterhead .divider{position:absolute;left:136px;top:8px;width:1px;height:34px;background:rgba(255,255,255,.8)}
.letterhead .contact{position:absolute;left:151px;top:8px}
.salutation{position:absolute;left:54px;top:168px;font-family:"Didact Gothic",sans-serif;font-size:11.5px;color:var(--ink)}
.body{position:absolute;left:54px;top:204px;width:374px;font-family:"Didact Gothic",sans-serif;font-size:6.4px;line-height:9.6px;color:#666}
.body p{margin-bottom:9.6px}
.signoff{position:absolute;left:54px;top:407px;font-family:"Didact Gothic",sans-serif;font-size:6.4px;color:#666}
.signature{position:absolute;left:50px;top:420px;width:82px;height:34px;background:linear-gradient(90deg,rgba(31,79,160,.18),rgba(31,79,160,.08));border-radius:3px}

.footer-rule{position:absolute;height:1px;background:var(--rule)}
.partners{position:absolute;display:flex;gap:6px;align-items:center}
.partner{height:15px;border-radius:2px;background:var(--partner)}
.partner.red{background:var(--red)}
.partner.blue{background:#6b8fb8;height:11px}
.member{position:absolute;width:102px;height:24px;background:var(--red);border-radius:2px}

/* cards */
.card-front{left:594px;top:114px;width:250px;height:143px}
.card-front .tab{top:22px;height:102px}
.card-front .band{top:22px;width:128px;height:102px;padding:14px 0 0 13px}
.card-front .brand{left:20px;top:62px}
.person{font-family:"Roboto Condensed",sans-serif;font-weight:700;font-size:9px;line-height:1.1}
.role{font-size:6px;margin-top:1px}
.card-front .address{margin-top:6px;font-size:5.6px}
.card-front .contact{margin-top:3px;font-size:5.6px}
.card-front .contact li{height:8px}

.card-back{left:866px;top:114px;width:250px;height:143px}
.card-back .partners{left:42px;top:58px}
.card-back .partners .partner{width:50px;height:17px}
.card-back .partners .partner.blue{width:56px;height:13px}
.slogans{position:absolute;left:0;right:0;top:116px;text-align:center;font-size:6.8px;color:#555;letter-spacing:.2px}

/* envelopes */
.envelope-back{left:601px;top:312px;width:530px;height:230px}
.flap{position:absolute;left:0;top:0}
.envelope-front{left:547px;top:426px;width:530px;height:231px}
.envelope-front .tab{top:23px;height:51px}
.envelope-front .band{top:23px;width:376px;height:51px;padding:16px 0 0 15px;font-weight:500}
.envelope-front .brand{left:27px;top:35px}
</style>
</head>
<body>
<main class="canvas">

  <!-- Letterhead -->
  <section class="sheet letterhead" aria-label="Letterhead">
    <div class="tab"></div>
    <div class="brand"><span class="brand-dot" style="width:26px;height:26px"></span><span class="brand-name" style="font-size:18px">nova crest</span></div>
    <div class="band">
      <div class="address">Ras Hamdan - Next to Corniche Plaza Mall<br>Noor Trade Tower Building - 604<br>P.O.Box : 47819 Dubai - U.A.E</div>
      <div class="divider"></div>
      <ul class="contact">
        <li><svg viewBox="0 0 10 10"><path d="M2 0h2l1 3-1.5 1a6 6 0 0 0 2.5 2.5L7 5l3 1v2c0 1-1 2-2 2C4 10 0 6 0 2c0-1 1-2 2-2z"/></svg>00971 4 58 71 204</li>
        <li><svg viewBox="0 0 10 10"><rect x="2" y="0" width="6" height="3"/><rect x="0" y="4" width="10" height="4" rx="1"/><rect x="2" y="7" width="6" height="3"/></svg>00971 4 58 71 205</li>
        <li><svg viewBox="0 0 10 10"><path d="M0 2h10v6H0z M0 2l5 3.5L10 2" stroke="#0a6fc2" stroke-width=".8"/></svg>info@novacrestcleansers.example</li>
        <li><svg viewBox="0 0 10 10"><circle cx="5" cy="5" r="5"/></svg>www.novacrestcleansers.example</li>
      </ul>
    </div>

    <p class="salutation">Dear Mr. Harlow,</p>
    <div class="body">
      <p>Lorem ipsum dolor sit amet, consectetur adipiscing elit. Donec orci purus, luctus vitae dignissim eu, iaculis sed purus. Vivamus faucibus, ipsum nec aliquet viverra, leo mauris condimentum ligula, sit amet sagittis enim ligula quis arcu. Nam egestas tortor id nisi porttitor mattis. In tortor ante, ultricies in suscipit a, tempus non massa. Vivamus et auctor mi. Fusce vel massa nulla. Phasellus nec eros mauris, et scelerisque orci.</p>
      <p>Donec malesuada orci vitae nulla accumsan porta a id massa. Quisque accumsan iaculis magna sit amet fringilla. Maecenas consequat, magna eget tincidunt semper, odio nibh rutrum mi, id feugiat ante nisi eu risus. Vestibulum nunc orci, rhoncus a placerat in, ultricies in mi. Cras mattis varius eros, vel fringilla nisi suscipit eget. Quisque scelerisque sagittis nulla at porttitor.</p>
      <p>Sed id augue vitae urna euismod commodo aliquet a quam. Pellentesque arcu velit, cursus et malesuada ut, consequat et diam. Nullam erat sem, rhoncus id ullamcorper vitae, rhoncus et arcu. In ultricies ultricies nulla, ut rutrum nisi iaculis at. Donec eu magna a metus ornare faucibus. Fusce aliquet faucibus ultricies. Morbi semper, est id tincidunt gravida, sem arcu adipiscing lacus, ac bibendum nulla leo eu purus. Quisque nec diam sed risus consectetur a accumsan quis quis nibh. Vestibulum id purus lorem.</p>
      <p>It is a long established fact that a reader will be distracted by the readable content of a page when looking at its layout. The point of using Lorem Ipsum is that it has a more-or-less normal distribution of letters, as opposed to using 'Content here, content here', making it look like readable English. Many desktop publishing packages</p>
    </div>
    <p class="signoff">Sincerely,</p>
    <div class="signature" role="img" aria-label="Handwritten signature of Peter Harlow"></div>

    <div class="footer-rule" style="left:41px;top:526px;width:374px"></div>
    <div class="partners" style="left:41px;top:545px">
      <span class="partner" style="width:50px"></span>
      <span class="partner red" style="width:46px"></span>
      <span class="partner blue" style="width:58px"></span>
    </div>
    <div class="member" style="left:313px;top:543px" role="img" aria-label="Khalid Bin Nasser Membership badge"></div>
  </section>

  <!-- Business card front -->
  <section class="sheet card-front" aria-label="Business card front">
    <div class="tab"></div>
    <div class="brand"><span class="brand-dot" style="width:20px;height:20px"></span><span class="brand-name" style="font-size:14px">nova crest</span></div>
    <div class="band">
      <div class="person">Samir Youssef Abdul Karim</div>
      <div class="role">DIRECTOR MANAGER<br>+ 971 52 387 0 387</div>
      <div class="address">Ras Hamdan - Next to Corniche Plaza Mall<br>Noor Trade Tower Building - 604<br>P.O.Box : 47819 Dubai - U.A.E</div>
      <ul class="contact">
        <li><svg viewBox="0 0 10 10"><path d="M2 0h2l1 3-1.5 1a6 6 0 0 0 2.5 2.5L7 5l3 1v2c0 1-1 2-2 2C4 10 0 6 0 2c0-1 1-2 2-2z"/></svg>00971 4 58 71 204</li>
        <li><svg viewBox="0 0 10 10"><rect x="2" y="0" width="6" height="10" rx="1"/></svg>00971 4 58 71 205</li>
        <li><svg viewBox="0 0 10 10"><path d="M0 2h10v6H0z"/></svg>info@novacrestcleansers.example</li>
        <li><svg viewBox="0 0 10 10"><circle cx="5" cy="5" r="5"/></svg>www.novacrestcleansers.example</li>
      </ul>
    </div>
  </section>

  <!-- Business card back -->
  <section class="sheet card-back" aria-label="Business card back">
    <div class="partners">
      <span class="partner"></span>
      <span class="partner red"></span>
      <span class="partner blue"></span>
    </div>
    <p class="slogans">ORU FRESH HOME &nbsp;-&nbsp; ORU PROFESSIONAL &nbsp;-&nbsp; FARAHEED</p>
  </section>

  <!-- Envelope back -->
  <section class="sheet envelope-back" aria-label="Envelope back">
    <svg class="flap" width="530" height="80" viewBox="0 0 530 80">
      <path d="M0 0H530L518 66Q516 76 506 76H24Q14 76 12 66Z" fill="var(--blue)"/>
      <circle cx="265" cy="40" r="17" fill="var(--green)"/>
    </svg>
  </section>

  <!-- Envelope front -->
  <section class="sheet envelope-front" aria-label="Envelope front">
    <div class="tab"></div>
    <div class="brand"><span class="brand-dot" style="width:26px;height:26px"></span><span class="brand-name" style="font-size:18px">nova crest</span></div>
    <div class="band">Ras Hamdan - Next to Corniche Plaza Mall<br>Noor Trade Tower Building - 604<br>P.O.Box : 47819 Dubai - U.A.E</div>
    <div class="footer-rule" style="left:27px;top:173px;width:476px"></div>
    <div class="partners" style="left:27px;top:192px">
      <span class="partner" style="width:50px"></span>
      <span class="partner red" style="width:46px"></span>
      <span class="partner blue" style="width:58px"></span>
    </div>
    <div class="member" style="left:401px;top:190px" role="img" aria-label="Khalid Bin Nasser Membership badge"></div>
  </section>

</main>
</body>
</html>
```